Handout Flyer For Medical Practice (This is Exciting!)

We need a single page handout that showcases the doctors in our medical practice and their specific specialities.

On the front I would like the pictures of the Doctors, names and their specialties. One the back, Map and Contact information for the practice

Attached in the files is what we are currently using and we do want anything that looks such as that.

Industry/Entity Type

Medical

Font styles to use
Serif

Colors
3176b5
0456a4

Requirements
Must have
• Up to date look. Would like a modern touch.

```html
<!DOCTYPE html>
<html lang="en">
<head>
<meta charset="utf-8">
<title>Crestview Sports Medicine &amp; Spine Care Institute</title>
<link href="https://fonts.googleapis.com/css2?family=Merriweather:wght@700;900&family=Source+Sans+3:wght@400;700&display=swap" rel="stylesheet">
<style>
  :root {
    --navy: #17306f;
    --swoosh: #cfd2d8;
    --paper: #ffffff;
    --ink: #1a1a1a;
    --photo-a: #9fb0ae;
    --photo-b: #5f6f78;
    --scene-sky: #bfe3ea;
    --scene-field: #3f6a3a;
  }
  html, body { margin: 0; padding: 0; overflow: hidden; background: #e9ecef; }
  .flyer {
    position: relative; width: 927px; height: 1200px; overflow: hidden;
    background: var(--navy);
    font-family: "Source Sans 3", Arial, sans-serif; color: var(--ink);
  }
  .backdrop { position: absolute; inset: 0; }
  .brand {
    position: absolute; left: 32px; top: 82px;
    display: flex; align-items: flex-start; gap: 14px;
  }
  .brand-dot { width: 20px; height: 20px; border-radius: 50%; background: #fff; margin-top: 18px; }
  .brand-name {
    font-family: "Merriweather", Georgia, serif; font-weight: 900;
    font-size: 26px; line-height: 34px; color: #fff; margin: 0;
  }
  .hero-photo {
    position: absolute; left: 479px; top: 18px; width: 426px; height: 307px;
    background: radial-gradient(ellipse at 50% 45%, var(--scene-sky) 0%, #8cc2d3 35%, var(--scene-field) 62%, var(--navy) 88%);
  }
  .intro {
    position: absolute; left: 0; top: 334px; width: 927px;
    color: #fff; font-size: 18px; line-height: 23.6px; margin: 0;
  }
  .intro span { position: absolute; white-space: nowrap; }
  .doctor-photo {
    position: absolute; width: 149px; height: 207px;
    background: linear-gradient(180deg, var(--photo-a) 0%, var(--photo-b) 100%);
  }
  .doctor-photo.light { background: linear-gradient(180deg, #f4f4f4 0%, #bfc4c9 100%); }
  .doctor-caption {
    position: absolute; font-size: 14px; line-height: 18px; margin: 0; color: var(--ink);
  }
  .doctor-caption strong { font-weight: 700; }
  .web-address {
    position: absolute; left: 560px; top: 1142px; width: 206px; text-align: center;
    color: #fff; font-weight: 700; font-size: 17px; line-height: 26px; letter-spacing: .2px;
  }
</style>
</head>
<body>
<main class="flyer">
  <svg class="backdrop" width="927" height="1200" viewBox="0 0 927 1200" aria-hidden="true">
    <path fill="var(--swoosh)" d="M0,200 C250,162 400,262 482,345 C575,440 665,555 752,680 C830,790 885,860 927,915 L927,1200 L440,1200 C230,1145 95,1010 0,852 Z"/>
    <path fill="var(--paper)" d="M0,222 C250,185 390,282 470,362 C560,455 650,570 735,695 C810,805 875,885 927,950 L927,1200 L420,1200 C220,1150 90,1022 0,872 Z"/>
    <rect x="330" y="1133" width="597" height="5" fill="var(--swoosh)"/>
    <path fill="var(--navy)" d="M300,1141 L927,1141 L927,1171 L352,1171 C335,1162 318,1152 300,1141 Z"/>
  </svg>

  <header class="brand">
    <span class="brand-dot"></span>
    <h1 class="brand-name">Crestview Sports Medicine<br>&amp; Spine Care Institute</h1>
  </header>

  <div class="hero-photo" role="img" aria-label="Photo of an active couple jogging together on a park lawn"></div>

  <p class="intro">
    <span style="left:573px;top:0">Crestview Sports Medicine &amp; Spine</span>
    <span style="left:573px;top:23.6px">Care Institute provides leading-edge,</span>
    <span style="left:573px;top:47.2px">results-based care for orthopedic and</span>
    <span style="left:573px;top:70.8px">spine disorders.&nbsp; We are a</span>
    <span style="left:588px;top:94.4px">comprehensive, premier team of</span>
    <span style="left:614px;top:118px">specialists dedicated to the</span>
    <span style="left:641px;top:141.6px">diagnosis, treatment,</span>
    <span style="left:668px;top:165.2px">rehabilitation and prevention</span>
    <span style="left:689px;top:188.8px">of sports and orthopedic</span>
    <span style="left:708px;top:212.4px">injuries and conditions.</span>
    <span style="left:727px;top:236px">Our team is dedicated</span>
    <span style="left:746px;top:259.6px">to improving the</span>
    <span style="left:764px;top:283.2px">quality of life for</span>
    <span style="left:783px;top:306.8px">our patients</span>
    <span style="left:801px;top:330.4px">and their</span>
    <span style="left:816px;top:354px">families.</span>
  </p>

  <div class="doctor-photo" style="left:44px;top:299px" role="img" aria-label="Portrait of Nathan R. Ellison"></div>
  <p class="doctor-caption" style="left:204px;top:460px"><strong>Nathan R. Ellison</strong>, MD<br>Orthopedic Surgeon</p>

  <div class="doctor-photo" style="left:44px;top:553px" role="img" aria-label="Portrait of Owen T. Marlowe"></div>
  <p class="doctor-caption" style="left:44px;top:768px"><strong>Owen T. Marlowe</strong>, MD<br>Physical Medicine and<br>Rehabilitation Specialist</p>

  <div class="doctor-photo" style="left:259px;top:553px" role="img" aria-label="Portrait of Lydia M. Prescott"></div>
  <p class="doctor-caption" style="left:256px;top:768px"><strong>Lydia M. Prescott</strong>, MD, MS<br>Physical Medicine and<br>Rehabilitation Specialist</p>

  <div class="doctor-photo" style="left:457px;top:553px" role="img" aria-label="Portrait of J. Adam Whitford"></div>
  <p class="doctor-caption" style="left:460px;top:768px"><strong>J. Adam Whitford</strong>, MD<br>Orthopedic Surgeon</p>

  <div class="doctor-photo light" style="left:265px;top:839px" role="img" aria-label="Portrait of Daniel P. Corwin"></div>
  <p class="doctor-caption" style="left:274px;top:1057px"><strong>Daniel P. Corwin</strong>, MD<br>Orthopedic Surgeon<br>Specializing in Spine</p>

  <div class="doctor-photo" style="left:479px;top:839px" role="img" aria-label="Portrait of Samuel K. Ritter"></div>
  <p class="doctor-caption" style="left:478px;top:1056px"><strong>Samuel K. Ritter</strong>, MD<br>Physical Medicine and<br>Rehabilitation Specialist</p>

  <div class="doctor-photo" style="left:680px;top:839px" role="img" aria-label="Portrait of Grant H. Delmore, Jr."></div>
  <p class="doctor-caption" style="left:681px;top:1057px"><strong>Grant H. Delmore</strong>, Jr., MD<br>Orthopedic Surgeon and Sports<br>Medicine and Shoulder Specialist</p>

  <div class="web-address">www.crestviewsportsmed.com</div>
</main>
</body>
</html>
```